Meadowlark Learning Growth Partners (MLGP)

This is a professional business card. Logo and picture are a must on the front of the card. I am an educational consultant. I have been consulting for the past three years for a company. I am now opening my own company. My goal for my consulting company is to eventually consult all over America.

Target Market(s)

Educators, schools, professionals

Industry/Entity Type

Consulting

Contact Information for Business Card

Picture/logo on front, simple modern design

Font styles to use
Serif

Colors
85abd2
0355a3
3176b5
cedeed

Requirements
Must have
• picture, logo,
• Odessa Pruitt, Ed.S
• address 5073 Cormorant ridge Dr. Nashville, TN 37940
• Cell:616-555-0148
• Office: 629-555-0172
• www.Mlgpedu.example
• pruittodessa@mailbox.example

```html
<!DOCTYPE html>
<html lang="en">
<head>
<meta charset="utf-8">
<title>Meadowlark Learning Growth Partners – Business Card</title>
<link href="https://fonts.googleapis.com/css2?family=Montserrat:wght@600;700;800&family=Tinos:wght@400&display=swap" rel="stylesheet">
<style>
  :root {
    --navy: #1e3c74;
    --navy-deep: #17305f;
    --paper: #ffffff;
    --stage: #e9edf2;
    --ink: #1e3c74;
    --photo-top: #d9c8b4;
    --photo-bottom: #2a2f3a;
  }
  * { box-sizing: border-box; margin: 0; padding: 0; }
  html, body { width: 1200px; height: 880px; overflow: hidden; }
  body { background: var(--stage); position: relative; font-family: "Tinos", "Times New Roman", serif; }

  .card {
    position: absolute;
    width: 600px; height: 343px;
    border-radius: 16px;
    overflow: hidden;
    box-shadow: 0 10px 30px rgba(20, 30, 60, 0.18);
  }

  /* Back of card */
  .card-back { left: 70px; top: 70px; background: var(--navy); }
  .card-back .brand {
    position: absolute; left: 0; right: 0; top: 118px;
    display: flex; align-items: center; justify-content: center; gap: 16px;
    color: var(--paper);
    font-family: "Montserrat", Arial, sans-serif; font-weight: 800;
    font-size: 64px; letter-spacing: 4px;
  }
  .card-back .brand-dot { width: 26px; height: 26px; border-radius: 50%; background: var(--paper); }
  .card-back .web {
    position: absolute; left: 0; right: 0; top: 246px; text-align: center;
    color: var(--paper); font-size: 15px; letter-spacing: 3px;
  }

  /* Front of card */
  .card-front { left: 530px; top: 450px; background: var(--paper); }
  .photo {
    position: absolute; right: 0; top: 18px; width: 232px; height: 250px;
    background: linear-gradient(180deg, var(--photo-top) 0%, #c9a98e 40%, var(--photo-bottom) 100%);
  }
  .web-block {
    position: absolute; right: 0; bottom: 0; width: 224px; height: 78px;
    background: var(--navy);
  }
  .web-block .web {
    position: absolute; right: 18px; top: 12px;
    color: var(--paper); font-size: 13px; letter-spacing: 2.5px;
  }
  .bottom-band {
    position: absolute; left: 0; bottom: 0; width: 368px; height: 14px;
    background: var(--navy);
  }

  .identity {
    position: absolute; left: 34px; top: 46px;
    display: flex; align-items: center; gap: 14px;
  }
  .identity .brand {
    display: flex; align-items: center; gap: 8px;
    color: var(--ink); font-family: "Montserrat", Arial, sans-serif;
    font-weight: 800; font-size: 30px; letter-spacing: 2px;
  }
  .identity .brand-dot { width: 14px; height: 14px; border-radius: 50%; background: var(--ink); }
  .identity .divider { width: 1.5px; height: 70px; background: var(--ink); }
  .identity .full-name {
    color: var(--ink); font-family: "Montserrat", Arial, sans-serif;
    font-weight: 700; font-size: 13px; line-height: 16px;
  }

  .person { position: absolute; left: 34px; top: 158px; width: 320px; }
  .person .rule { height: 1px; background: var(--ink); }
  .person .name {
    color: var(--ink); font-size: 19px; letter-spacing: 0.5px;
    padding: 6px 0 6px;
  }

  .contacts { position: absolute; left: 40px; top: 206px; list-style: none; }
  .contacts li {
    display: flex; align-items: center; gap: 10px;
    color: var(--ink); font-size: 14px; line-height: 22px;
  }
  .contacts svg { width: 12px; height: 12px; fill: var(--ink); flex: none; }
</style>
</head>
<body>

<section class="card card-back" aria-label="Card back">
  <div class="brand"><span class="brand-dot"></span>MLGP</div>
  <p class="web">www.Mlgpedu.example</p>
</section>

<section class="card card-front" aria-label="Card front">
  <div class="photo" role="img" aria-label="Portrait photograph of Odessa Pruitt"></div>
  <div class="web-block"><p class="web">www.Mlgpedu.example</p></div>
  <div class="bottom-band"></div>

  <div class="identity">
    <div class="brand"><span class="brand-dot"></span>MLGP</div>
    <div class="divider"></div>
    <p class="full-name">Meadowlark<br>Learning<br>Growth<br>Partners</p>
  </div>

  <div class="person">
    <div class="rule"></div>
    <p class="name">ODESSA PRUITT, ED.S</p>
    <div class="rule"></div>
  </div>

  <ul class="contacts">
    <li>
      <svg viewBox="0 0 12 12"><path d="M3 0h6a1 1 0 0 1 1 1v10a1 1 0 0 1-1 1H3a1 1 0 0 1-1-1V1a1 1 0 0 1 1-1zm0 2v7h6V2z"/></svg>
      616-555-0148
    </li>
    <li>
      <svg viewBox="0 0 12 12"><path d="M2.5 1l2 2.5-1.2 1.2a7 7 0 0 0 4 4L8.5 7.5 11 9.5 9.8 11.2C5 11 1 7 .8 2.2z"/></svg>
      629-555-0172
    </li>
    <li>
      <svg viewBox="0 0 12 12"><path d="M0 2h12v8H0zm1 1v.4l5 3.4 5-3.4V3z"/></svg>
      pruittodessa@mailbox.example
    </li>
    <li>
      <svg viewBox="0 0 12 12"><path d="M6 0a4 4 0 0 1 4 4c0 3-4 8-4 8S2 7 2 4a4 4 0 0 1 4-4zm0 2.5a1.5 1.5 0 1 0 0 3 1.5 1.5 0 0 0 0-3z"/></svg>
      5073 Cormorant ridge Dr. Nashville, TN 37940
    </li>
  </ul>
</section>

</body>
</html>
```